Brochure and Flyer template, Aluminium Facade company
Verdantis Structural Concepts pty Ltd
We are looking for a cutting edge Brochure and Flyer template that we can change text and pictures for different marketing products and services we provide to different target markets and audiences. We like a mixture of A4 size but also like the A5 size so please feel free to be creative.
Construction
Corporate, Building Companies, Architects, Home owners.
We are needing the Brochure template to cater for multiple product pictures and descriptions in either A4 or A5 format (please be creative) and the flier template is more aimed to focus on 1 or 2 individual products.
1 of 2 files of Past project photos for your use if you like
Our Logo
Our Logo Different Format
Our Company Profile (old and out dated for reference only!)
2 of 2 files of Past project photos for your use if you like
Past Projects for information on our company
SOME of our standard Products FOR YOUR INFORMATION ONLY
Havenor opening roof System Photos to go with the operable section Please make sure the Havenor logo is used
Our Products and Services description
Havenor opening Roof information
More Havenor opening roof pics and data. May be of use

```html
<!DOCTYPE html>
<html lang="en">
<head>
<meta charset="utf-8">
<title>Verdantis Structural Concepts – Brochure and Flyer Templates</title>
<link rel="stylesheet" href="https://fonts.googleapis.com/css2?family=Open+Sans:wght@400;600;700&display=swap">
<style>
  :root {
    --bg: #e9ebea;
    --green: #1c8a5e;
    --green-dark: #0f5f40;
    --green-light: #5cb68c;
    --charcoal: #3b3f42;
    --charcoal-dark: #26292b;
    --paper: #ffffff;
    --paper-grey: #f1f2f1;
    --ink: #3c3c3c;
    --ink-soft: #8a8d8c;
    --photo-a: #9fa9ad;
    --photo-b: #d7dcd9;
  }
  * { box-sizing: border-box; margin: 0; padding: 0; }
  html, body { width: 1200px; height: 506px; overflow: hidden; }
  body {
    background: var(--bg);
    font-family: "Open Sans", Arial, sans-serif;
    color: var(--ink);
    position: relative;
  }
  .sheet {
    position: absolute;
    display: flex;
    background: var(--paper);
    box-shadow: 0 2px 6px rgba(0,0,0,.18);
    overflow: hidden;
  }
  .page { position: relative; flex: 1; overflow: hidden; }
  .page + .page { border-left: 1px solid #dcdedd; }
  .photo {
    position: absolute;
    background: linear-gradient(160deg, var(--photo-b), var(--photo-a));
  }
  .photo.sky { background: linear-gradient(180deg, #c9d6de 0%, #a9b3b6 55%, #7f8789 100%); }
  .photo.green { background: linear-gradient(160deg, #8fb7a2, #4f7f67); }
  .swoosh { position: absolute; left: 0; width: 100%; display: block; }
  .logo {
    position: absolute;
    display: flex; align-items: center; gap: 4px;
    font-weight: 700; color: var(--green); letter-spacing: .5px;
  }
  .logo .mark { border-radius: 50%; background: var(--green); display: block; }
  .logo.light { color: var(--paper); }
  .logo.light .mark { background: var(--paper); }
  .heading { position: absolute; font-weight: 700; color: var(--green); }
  .body-text { position: absolute; font-size: 5px; line-height: 7px; color: var(--ink-soft); }
  .caption { position: absolute; font-size: 5px; font-weight: 600; color: var(--ink); }

  /* flyer */
  .flyer-outside { left: 20px; top: 20px; width: 380px; height: 232px; }
  .flyer-inside  { left: 20px; top: 262px; width: 380px; height: 224px; }
  .panel-about { background: linear-gradient(180deg, var(--charcoal) 0%, var(--charcoal-dark) 100%); }
  .panel-about .heading { color: var(--paper); }
  .panel-about .body-text { color: #c5c8c7; }

  /* brochure */
  .spread { width: 372px; height: 150px; }
  .col-a { left: 420px; } .col-b { left: 808px; }
  .row-1 { top: 20px; } .row-2 { top: 178px; } .row-3 { top: 336px; }
  .cover-band { background: linear-gradient(180deg, var(--green-light), var(--green) 45%, var(--green-dark)); }
  .swatches { position: absolute; display: flex; gap: 2px; }
  .swatches span { width: 8px; height: 26px; display: block; }
</style>
</head>
<body>

<!-- Flyer: outside -->
<section class="sheet flyer-outside">
  <div class="page panel-about">
    <h2 class="heading" style="left:12px;top:12px;font-size:9px;">About Us</h2>
    <p class="body-text" style="left:12px;top:28px;width:160px;">We design, supply and install aluminium facades for commercial and residential projects across the region.</p>
    <div class="photo sky" role="img" aria-label="Aluminium facade project photo" style="left:12px;top:62px;width:80px;height:50px;"></div>
    <div class="photo" role="img" aria-label="Louvre screen detail photo" style="left:98px;top:62px;width:80px;height:50px;"></div>
    <svg class="swoosh" style="bottom:0;height:100px" viewBox="0 0 190 100" preserveAspectRatio="none">
      <path d="M0 40 Q95 0 190 30 L190 100 L0 100Z" fill="#ffffff"/>
      <path d="M0 48 Q95 10 190 38" stroke="var(--green)" stroke-width="3" fill="none"/>
    </svg>
    <div class="logo" style="left:60px;top:178px;font-size:10px;"><span class="mark" style="width:9px;height:9px"></span>VERDANTIS</div>
    <p class="body-text" style="left:40px;top:198px;width:120px;text-align:center;">Phone 02 5550 1842 · info@verdantis-sc.example</p>
  </div>
  <div class="page">
    <div class="logo" style="left:56px;top:12px;font-size:12px;"><span class="mark" style="width:11px;height:11px"></span>VERDANTIS</div>
    <div class="photo sky" role="img" aria-label="Operable aluminium roof over a courtyard" style="left:0;top:38px;width:100%;height:110px;"></div>
    <svg class="swoosh" style="bottom:0;height:96px" viewBox="0 0 190 96" preserveAspectRatio="none">
      <path d="M0 30 Q100 0 190 22 L190 96 L0 96Z" fill="var(--green)"/>
      <path d="M0 40 Q100 8 190 30" stroke="#ffffff" stroke-width="3" fill="none"/>
      <path d="M0 70 Q100 50 190 66 L190 96 L0 96Z" fill="var(--charcoal)"/>
    </svg>
  </div>
</section>

<!-- Flyer: inside -->
<section class="sheet flyer-inside">
  <div class="page">
    <h2 class="heading" style="left:12px;top:10px;font-size:9px;">Our Products</h2>
    <p class="body-text" style="left:12px;top:26px;width:160px;">Louvres, screens, cladding and operable roof systems built to order.</p>
    <div class="photo sky" role="img" aria-label="Product photo" style="left:12px;top:48px;width:52px;height:38px;"></div>
    <div class="photo" role="img" aria-label="Product photo" style="left:68px;top:48px;width:52px;height:38px;"></div>
    <div class="photo sky" role="img" aria-label="Product photo" style="left:124px;top:48px;width:52px;height:38px;"></div>
    <div class="photo" role="img" aria-label="Product photo" style="left:12px;top:96px;width:52px;height:38px;"></div>
    <div class="photo sky" role="img" aria-label="Product photo" style="left:68px;top:96px;width:52px;height:38px;"></div>
    <div class="photo" role="img" aria-label="Product photo" style="left:124px;top:96px;width:52px;height:38px;"></div>
    <svg class="swoosh" style="bottom:0;height:60px" viewBox="0 0 190 60" preserveAspectRatio="none">
      <path d="M0 28 Q95 8 190 24 L190 60 L0 60Z" fill="var(--green)"/>
      <path d="M0 36 Q95 16 190 32" stroke="#ffffff" stroke-width="2" fill="none"/>
    </svg>
  </div>
  <div class="page">
    <h2 class="heading" style="left:12px;top:10px;font-size:9px;">Our Services</h2>
    <p class="body-text" style="left:12px;top:26px;width:160px;">Design advice, shop drawings, fabrication and on-site installation.</p>
    <div class="photo" role="img" aria-label="Installation photo" style="left:12px;top:48px;width:80px;height:40px;"></div>
    <div class="photo sky" role="img" aria-label="Completed building photo" style="left:96px;top:48px;width:80px;height:40px;"></div>
    <div class="photo sky" role="img" aria-label="Completed building photo" style="left:12px;top:96px;width:80px;height:40px;"></div>
    <div class="photo" role="img" aria-label="Facade detail photo" style="left:96px;top:96px;width:80px;height:40px;"></div>
    <svg class="swoosh" style="bottom:0;height:60px" viewBox="0 0 190 60" preserveAspectRatio="none">
      <path d="M0 24 Q95 8 190 28 L190 60 L0 60Z" fill="var(--green)"/>
      <path d="M0 32 Q95 16 190 36" stroke="#ffffff" stroke-width="2" fill="none"/>
    </svg>
  </div>
</section>

<!-- Brochure: cover -->
<section class="sheet spread col-a row-1">
  <div class="page cover-band">
    <div class="logo light" style="left:62px;top:64px;font-size:11px;"><span class="mark" style="width:10px;height:10px"></span>VERDANTIS</div>
  </div>
  <div class="page">
    <div class="page cover-band" style="position:absolute;left:0;top:0;width:100%;height:40px;"></div>
    <div class="logo light" style="left:60px;top:13px;font-size:12px;"><span class="mark" style="width:11px;height:11px"></span>VERDANTIS</div>
    <div class="photo sky" role="img" aria-label="Operable aluminium roof photo" style="left:0;top:40px;width:100%;height:86px;"></div>
    <svg class="swoosh" style="bottom:0;height:30px" viewBox="0 0 186 30" preserveAspectRatio="none">
      <path d="M0 12 Q93 0 186 10 L186 30 L0 30Z" fill="var(--green)"/>
    </svg>
  </div>
</section>

<!-- Brochure: feature + colours -->
<section class="sheet spread col-b row-1">
  <div class="page">
    <div class="photo sky" role="img" aria-label="Large project photo of aluminium louvres" style="left:0;top:0;width:100%;height:100%;"></div>
  </div>
  <div class="page">
    <h2 class="heading" style="left:12px;top:12px;font-size:8px;">Colour Range</h2>
    <p class="body-text" style="left:12px;top:26px;width:90px;">Durable powder-coated aluminium profiles in a wide range of colours.</p>
    <div class="swatches" style="left:12px;top:62px;">
      <span style="background:#2f3b4a"></span><span style="background:#6d7b86"></span><span style="background:#b7362f"></span><span style="background:#d9a441"></span><span style="background:#3f7f4f"></span><span style="background:#8a5a3b"></span><span style="background:#c9cfd2"></span>
    </div>
    <div class="photo green" role="img" aria-label="Coloured facade panels photo" style="left:112px;top:12px;width:62px;height:80px;"></div>
    <svg class="swoosh" style="bottom:0;height:30px" viewBox="0 0 186 30" preserveAspectRatio="none">
      <path d="M0 14 Q93 0 186 12 L186 30 L0 30Z" fill="var(--green)"/>
    </svg>
  </div>
</section>

<!-- Brochure: products spread -->
<section class="sheet spread col-a row-2">
  <div class="page" style="background:var(--paper-grey)">
    <h2 class="heading" style="left:12px;top:10px;font-size:8px;">Our Products</h2>
    <div class="photo sky" role="img" aria-label="Product photo" style="left:12px;top:26px;width:76px;height:42px;"></div>
    <div class="photo" role="img" aria-label="Product photo" style="left:96px;top:26px;width:76px;height:42px;"></div>
    <span class="caption" style="left:12px;top:71px;">Sliding screens</span>
    <span class="caption" style="left:96px;top:71px;">Fixed louvres</span>
    <p class="body-text" style="left:12px;top:82px;width:160px;">Durable powder-coated aluminium profiles in a wide range of colours.</p>
    <svg class="swoosh" style="bottom:0;height:28px" viewBox="0 0 186 28" preserveAspectRatio="none">
      <path d="M0 10 Q93 0 186 12 L186 28 L0 28Z" fill="var(--green)"/>
    </svg>
  </div>
  <div class="page" style="background:var(--paper-grey)">
    <div class="photo sky" role="img" aria-label="Opening roof photo" style="left:12px;top:12px;width:162px;height:60px;"></div>
    <span class="caption" style="left:12px;top:76px;">Opening roof</span>
    <svg class="swoosh" style="bottom:0;height:28px" viewBox="0 0 186 28" preserveAspectRatio="none">
      <path d="M0 12 Q93 0 186 10 L186 28 L0 28Z" fill="var(--green)"/>
    </svg>
  </div>
</section>

<!-- Brochure: projects spread -->
<section class="sheet spread col-b row-2">
  <div class="page">
    <svg class="swoosh" style="top:0;height:22px" viewBox="0 0 186 22" preserveAspectRatio="none">
      <path d="M0 0 L186 0 L186 10 Q93 22 0 12Z" fill="var(--green)"/>
    </svg>
    <h2 class="heading" style="left:12px;top:26px;font-size:8px;">Our Projects</h2>
    <div class="photo sky" role="img" aria-label="Project photo" style="left:12px;top:42px;width:76px;height:46px;"></div>
    <div class="photo" role="img" aria-label="Project photo" style="left:96px;top:42px;width:76px;height:46px;"></div>
    <span class="caption" style="left:12px;top:92px;">Facade cladding</span>
    <span class="caption" style="left:96px;top:92px;">Privacy panels</span>
  </div>
  <div class="page">
    <svg class="swoosh" style="top:0;height:22px" viewBox="0 0 186 22" preserveAspectRatio="none">
      <path d="M0 0 L186 0 L186 12 Q93 22 0 10Z" fill="var(--green)"/>
    </svg>
    <div class="photo sky" role="img" aria-label="Project photo" style="left:12px;top:30px;width:162px;height:58px;"></div>
    <span class="caption" style="left:12px;top:92px;">Sun shading</span>
    <p class="body-text" style="left:12px;top:102px;width:160px;">Durable powder-coated aluminium profiles in a wide range of colours.</p>
  </div>
</section>

<!-- Brochure: services spread -->
<section class="sheet spread col-a row-3">
  <div class="page cover-band">
    <h2 class="heading" style="left:12px;top:14px;font-size:8px;color:var(--paper);">Our Services</h2>
    <div class="photo" role="img" aria-label="Service photo" style="left:12px;top:32px;width:162px;height:60px;"></div>
  </div>
  <div class="page">
    <div class="photo sky" role="img" aria-label="Service photo" style="left:12px;top:14px;width:76px;height:46px;"></div>
    <div class="photo" role="img" aria-label="Service photo" style="left:96px;top:14px;width:76px;height:46px;"></div>
    <p class="body-text" style="left:12px;top:68px;width:160px;">Durable powder-coated aluminium profiles in a wide range of colours.</p>
    <svg class="swoosh" style="bottom:0;height:28px" viewBox="0 0 186 28" preserveAspectRatio="none">
      <path d="M0 12 Q93 0 186 10 L186 28 L0 28Z" fill="var(--green)"/>
    </svg>
  </div>
</section>

<!-- Brochure: back spread -->
<section class="sheet spread col-b row-3">
  <div class="page">
    <div class="photo sky" role="img" aria-label="Building photo" style="left:12px;top:14px;width:76px;height:52px;"></div>
    <div class="photo sky" role="img" aria-label="Building photo" style="left:96px;top:14px;width:76px;height:52px;"></div>
    <svg class="swoosh" style="bottom:0;height:28px" viewBox="0 0 186 28" preserveAspectRatio="none">
      <path d="M0 10 Q93 0 186 12 L186 28 L0 28Z" fill="var(--green)"/>
    </svg>
  </div>
  <div class="page cover-band">
    <div class="logo light" style="left:62px;top:64px;font-size:11px;"><span class="mark" style="width:10px;height:10px"></span>VERDANTIS</div>
  </div>
</section>

</body>
</html>
```